Brochure Design - Marketing Document - real estate development

It is a 7 Page Proposal document. Please see attached example. It will be used as a marketing proposal document given to potential clients. It is a 'capability statement' used to demonstrate the capability and expertise of the business. I will provide all images and copy to be used in the document. I just need someone to create the template. Use the attached document as a guide for design, style, look and feel

Company name: Tarnwick Communities

I'll be happy to receive the document 80% complete so I can fill in the copy and minor details. All I need from a designer is to format and design a template that I can fill in

Thank you!

Target Market(s)

Corporate investors/clients

Font styles to use
Serif
Sans Serif

Requirements
Must have
• Please use the images of elderly people I have uploaded. There doesn't need to be a photo on every page, but please incorporate the images as you see fit. Also please use the logo attached 'Tarnwick Communities'
• Please see below the template layout/order page by page
• 1st page
• • Branding, photo of beach, headline saying capability statement
• 2nd page
• ABOUT US
• • High level overview from market/retail perspective of what Tarnwick offers and who we are
• • Talk about product and company philosophy
• 3rd page
• OUR TEAM
• • Photos, names and roles
• • Speak generally about immense team experience as a composite body of achievement
• 4th Page
• • List of projects and project values
• Page 5
• • More projects and project values
• Page 6
• • What we are offering our JV partners
• • Benefits and options of model
• Page 7
• • How Tarwick will change the market for the better/ difference between us and old models
• Final page
• • Branding, Address, company details. ABN/CAN
Should not have
• Please do NOT use bright/electric colours of blue, green or orange.
• Please use the attached document as a guide for style, colours and layout

```html
<!DOCTYPE html>
<html lang="en">
<head>
<meta charset="utf-8">
<title>Tarnwick Communities – Capability Statement</title>
<link href="https://fonts.googleapis.com/css2?family=Cinzel:wght@400;500&family=Open+Sans:wght@300;400;600&display=swap" rel="stylesheet">
<style>
:root{
  --page:#d8d8d8;
  --band:#f1f1f1;
  --strip:#d4d4d4;
  --dark:#636363;
  --darker:#5a5a5a;
  --mid:#a9a9a9;
  --ink:#4a4a4a;
  --body:#5a5a5a;
  --white:#ffffff;
  --serif:'Cinzel', serif;
  --sans:'Open Sans', sans-serif;
}
*{margin:0;padding:0;box-sizing:border-box}
html,body{width:1200px;height:947px;overflow:hidden;background:var(--white)}
.canvas{position:relative;width:1200px;height:947px}
.page{position:absolute;width:272px;height:385px;background:var(--page);overflow:hidden}
.p1{left:27px;top:38px}.p2{left:314px;top:38px}.p3{left:602px;top:38px}.p4{left:891px;top:38px}
.p5{left:27px;top:498px}.p6{left:314px;top:498px}.p7{left:602px;top:498px}.p8{left:893px;top:498px}
.abs{position:absolute}
.strip{position:absolute;left:0;top:0;width:100%;height:30px;background:var(--strip)}
.url{position:absolute;top:13px;font:600 3.8px/1 var(--serif);color:var(--ink);letter-spacing:.2px}
.url.left{left:14px}.url.right{right:14px}
.pageno{position:absolute;top:7px;width:21px;height:14px;background:var(--dark);color:var(--white);font:400 8px/14px var(--sans);text-align:center}
.pageno.right{right:4px}.pageno.left{left:4px}
.band{position:absolute;left:0;width:100%;background:var(--band)}
.title{font:400 14.5px/1.3 var(--serif);color:var(--ink);letter-spacing:.6px}
.title.center{text-align:center}
.footbar{position:absolute;left:0;bottom:0;width:100%;height:6px;background:var(--dark)}
.txt{position:absolute;font:400 4.3px/1.5 var(--sans);color:var(--body);text-align:justify;overflow:hidden}
.txt.light{color:#eeeeee}
.photo{position:absolute}
.brand{position:absolute;left:0;width:100%;text-align:center;color:#6e6e6e}
.brand-name{font:400 17px/1 var(--serif);letter-spacing:4px}
.brand-sub{font:400 5px/1 var(--sans);letter-spacing:3px;margin-top:5px}
.h-sans{position:absolute;font:400 10px/1.25 var(--sans);color:var(--ink)}
.member .name{font:600 6px/1 var(--sans);color:#333;text-align:center}
.member .role{font:300 6px/1.4 var(--sans);color:#444;text-align:center}
.member{position:absolute;width:66px}
.member .shot{width:66px;height:74px;background:linear-gradient(160deg,#c9c2b8,#6f6a66 60%,#3c3f48)}
.member .label{margin-top:7px}
.circle{position:absolute;width:70px;height:70px;border-radius:50%;border:4px solid #c7c7c7;box-shadow:0 0 0 1px #bdbdbd}
.col-head{position:absolute;font:400 9.5px/1 var(--sans);color:var(--ink);text-align:center}
.outline-box{position:absolute;border:1px solid #8a8a8a;border-radius:3px}
.contact-title{font:400 16px/1 var(--serif);color:var(--white)}
.contact-line{font:400 5.6px/1.35 var(--sans);color:var(--white)}
.social{display:inline-block;width:12px;height:12px;background:#555;margin-left:3px;vertical-align:-1px}
</style>
</head>
<body>
<div class="canvas">

<!-- Page 1 : cover -->
<section class="page p1">
  <div class="brand" style="top:21px"><div class="brand-name">TARNWICK</div><div class="brand-sub">COMMUNITIES</div></div>
  <div class="abs" style="left:0;top:128px;width:272px;height:165px;background:#7b7b7b"></div>
  <div class="photo" role="img" aria-label="Elderly couple sitting together on a beach at dusk" style="left:14px;top:56px;width:242px;height:277px;background:linear-gradient(180deg,#2f4f72 0%,#4f6e8e 40%,#7d8a93 62%,#6b6a6a 80%,#4c4c50 100%)"></div>
  <div class="abs" style="left:26px;top:255px;font:300 18px/1 var(--sans);color:var(--white)">Capability</div>
  <div class="abs" style="left:25px;top:277px;font:400 33px/1 var(--serif);color:var(--white);letter-spacing:2px">STATEMENT</div>
  <div class="abs" style="left:26px;top:317px;font:400 4.6px/1 var(--sans);color:#e8e8e8">Lorem Ipsum is simply dummy text of the printing and typesetting industry.</div>
  <div class="abs" style="left:0;top:358px;width:272px;text-align:center;font:400 6px/1 var(--serif);color:#666;letter-spacing:1px">WWW.TARNWICKCOMMUNITIES.COM</div>
</section>

<!-- Page 2 : about us -->
<section class="page p2">
  <div class="strip"></div>
  <div class="url left">WWW.TARNWICKCOMMUNITIES.COM</div>
  <div class="pageno right">02</div>
  <div class="band" style="top:30px;height:52px"><div class="title center" style="padding-top:18px">ABOUT US</div></div>
  <div class="photo" role="img" aria-label="Smiling senior couple playing golf" style="left:11px;top:104px;width:111px;height:98px;background:linear-gradient(170deg,#e7efe0 0%,#c7d6b6 45%,#b9a9c9 70%,#e2d2a6 100%)"></div>
  <div class="h-sans" style="left:11px;top:209px;width:115px">High level overview from market/retail perspective of what Tarnwick offers and who we are</div>
  <div class="txt" style="left:11px;top:276px;width:112px;height:84px">Lorem Ipsum is simply dummy text of the printing and typesetting industry. Lorem Ipsum has been the industry's standard dummy text ever since the 1500s, when an unknown printer took a galley of type and scrambled it to make a type specimen book. It has survived not only five centuries, but also the leap into electronic typesetting, remaining essentially unchanged. It was popularised in the 1960s with the release of Letraset sheets containing Lorem Ipsum passages, and more recently with desktop publishing software like Aldus PageMaker including versions of Lorem Ipsum.</div>
  <div class="abs" style="left:130px;top:104px;width:134px;height:257px;background:var(--dark)"></div>
  <div class="h-sans" style="left:136px;top:109px;width:126px;color:var(--white);font-size:10.5px">Talk about product and company philosophy</div>
  <div class="txt light" style="left:136px;top:136px;width:122px;height:220px">Lorem Ipsum is simply dummy text of the printing and typesetting industry. Lorem Ipsum has been the industry's standard dummy text ever since the 1500s, when an unknown printer took a galley of type and scrambled it to make a type specimen book. It has survived not only five centuries, but also the leap into electronic typesetting, remaining essentially unchanged. It was popularised in the 1960s with the release of Letraset sheets containing Lorem Ipsum passages, and more recently with desktop publishing software like Aldus PageMaker including versions of Lorem Ipsum. Lorem Ipsum is simply dummy text of the printing and typesetting industry. Lorem Ipsum has been the industry's standard dummy text ever since the 1500s, when an unknown printer took a galley of type and scrambled it to make a type specimen book. It has survived not only five centuries, but also the leap into electronic typesetting, remaining essentially unchanged. It was popularised in the 1960s with the release of Letraset sheets containing Lorem Ipsum passages, and more recently with desktop publishing software like Aldus PageMaker including versions of Lorem Ipsum. Lorem Ipsum is simply dummy text of the printing and typesetting industry. Lorem Ipsum has been the industry's standard dummy text ever since the 1500s, when an unknown printer took a galley of type and scrambled it to make a type specimen book. It has survived not only five centuries, but also the leap into electronic typesetting, remaining essentially unchanged. It was popularised in the 1960s with the release of Letraset sheets containing Lorem Ipsum passages, and more recently with desktop publishing software like Aldus PageMaker including versions of Lorem Ipsum.</div>
  <div class="footbar"></div>
</section>

<!-- Page 3 : our team -->
<section class="page p3">
  <div class="strip"></div>
  <div class="pageno left">03</div>
  <div class="url right">WWW.TARNWICKCOMMUNITIES.COM</div>
  <div class="band" style="top:30px;height:52px"><div class="title center" style="padding-top:18px">OUR TEAM</div></div>
  <div class="member" style="left:18px;top:90px"><div class="shot" role="img" aria-label="Portrait of team member"></div><div class="label"><div class="name">Daniel Reyes</div><div class="role">General manager</div></div></div>
  <div class="member" style="left:96px;top:90px"><div class="shot" role="img" aria-label="Portrait of team member"></div><div class="label"><div class="name">Omar Haddad</div><div class="role">Marketing manager</div></div></div>
  <div class="member" style="left:174px;top:90px"><div class="shot" role="img" aria-label="Portrait of team member"></div><div class="label"><div class="name">Lukas Brenner</div><div class="role">Technical supervisor</div></div></div>
  <div class="member" style="left:18px;top:201px"><div class="shot" role="img" aria-label="Portrait of team member"></div><div class="label"><div class="name">Victor Lindqvist</div><div class="role">General manager</div></div></div>
  <div class="member" style="left:96px;top:201px"><div class="shot" role="img" aria-label="Portrait of team member"></div><div class="label"><div class="name">Omar Haddad</div><div class="role">Marketing manager</div></div></div>
  <div class="member" style="left:174px;top:201px"><div class="shot" role="img" aria-label="Portrait of team member"></div><div class="label"><div class="name">Lukas Brenner</div><div class="role">Technical supervisor</div></div></div>
  <div class="abs" style="left:0;top:321px;width:272px;height:35px;background:var(--dark)"></div>
  <div class="txt light" style="left:13px;top:326px;width:246px;height:26px">Lorem Ipsum is simply dummy text of the printing and typesetting industry. Lorem Ipsum has been the industry's standard dummy text ever since the 1500s, when an unknown printer took a galley of type and scrambled it to make a type specimen book.</div>
  <div class="footbar"></div>
</section>

<!-- Page 4 : projects -->
<section class="page p4">
  <div class="strip"></div>
  <div class="url left">WWW.TARNWICKCOMMUNITIES.COM</div>
  <div class="pageno right">04</div>
  <div class="band" style="top:30px;height:52px"><div class="title" style="padding:18px 0 0 21px;font-size:13.5px">PROJECTS &amp; PROJECT VALUES</div></div>
  <div class="txt" style="left:21px;top:90px;width:236px;height:38px">Lorem Ipsum is simply dummy text of the printing and typesetting industry. Lorem Ipsum has been the industry's standard dummy text ever since the 1500s, when an unknown printer took a galley of type and scrambled it to make a type specimen book. It has survived not only five centuries, but also the leap into electronic typesetting, remaining essentially unchanged. It was popularised in the 1960s with the release of Letraset sheets containing Lorem Ipsum passages, and more recently with desktop publishing software like Aldus PageMaker including versions of Lorem Ipsum.</div>
  <div class="abs" style="left:0;top:176px;width:272px;height:3px;background:#8f8f8f"></div>
  <div class="circle" role="img" aria-label="Senior couple on a golf course" style="left:23px;top:143px;background:linear-gradient(170deg,#dfe9d6,#b6a7c4 60%,#e3d3a7)"></div>
  <div class="circle" role="img" aria-label="Senior swimmer at a pool" style="left:106px;top:143px;background:linear-gradient(170deg,#d8e7f1,#7fb0d6 55%,#c9a68c)"></div>
  <div class="circle" role="img" aria-label="Senior cyclists in a park" style="left:187px;top:143px;background:linear-gradient(170deg,#cfe0b4,#8fae6c 60%,#d7d2c4)"></div>
  <div class="col-head" style="left:18px;top:218px;width:80px">Lorem Ipsum</div>
  <div class="col-head" style="left:100px;top:218px;width:80px">Lorem Ipsum</div>
  <div class="col-head" style="left:182px;top:218px;width:80px">Lorem Ipsum</div>
  <div class="txt" style="left:24px;top:233px;width:70px;height:64px">Lorem Ipsum is simply dummy text of the printing and typesetting industry. Lorem Ipsum has been the industry's standard dummy text ever since the 1500s, when an unknown printer took a galley of type and scrambled it to make a type specimen book.</div>
  <div class="txt" style="left:106px;top:233px;width:70px;height:64px">Lorem Ipsum is simply dummy text of the printing and typesetting industry. Lorem Ipsum has been the industry's standard dummy text ever since the 1500s, when an unknown printer took a galley of type and scrambled it to make a type specimen book.</div>
  <div class="txt" style="left:188px;top:233px;width:70px;height:64px">Lorem Ipsum is simply dummy text of the printing and typesetting industry. Lorem Ipsum has been the industry's standard dummy text ever since the 1500s, when an unknown printer took a galley of type and scrambled it to make a type specimen book.</div>
  <div class="col-head" style="left:0;top:354px;width:272px;top:354px"></div>
  <div class="outline-box" style="left:22px;top:326px;width:238px;height:36px"></div>
  <div class="abs" style="left:104px;top:320px;width:66px;background:var(--page);font:400 9.5px/1 var(--sans);color:var(--ink);text-align:center">Lorem Ipsum</div>
  <div class="txt" style="left:32px;top:333px;width:220px;height:27px">Lorem Ipsum is simply dummy text of the printing and typesetting industry. Lorem Ipsum has been the industry's standard dummy text ever since the 1500s, when an unknown printer took a galley of type and scrambled it to make a type specimen book. It has survived not only five centuries, but also the leap into electronic typesetting, remaining essentially unchanged. It was popularised in the 1960s with the release of Letraset sheets containing Lorem Ipsum passages, and more recently with desktop publishing software like Aldus PageMaker including versions of Lorem Ipsum.</div>
  <div class="footbar"></div>
</section>

<!-- Page 5 : more projects -->
<section class="page p5">
  <div class="strip"></div>
  <div class="pageno left">05</div>
  <div class="url right">WWW.TARNWICKCOMMUNITIES.COM</div>
  <div class="band" style="top:30px;height:52px;background:var(--band)"><div class="title" style="padding:8px 0 0 21px;line-height:1.3">More Projects &amp; Project<br>Values</div></div>
  <div class="band" style="top:82px;height:53px"></div>
  <div class="txt" style="left:21px;top:88px;width:236px;height:40px">Lorem Ipsum is simply dummy text of the printing and typesetting industry. Lorem Ipsum has been the industry's standard dummy text ever since the 1500s, when an unknown printer took a galley of type and scrambled it to make a type specimen book. It has survived not only five centuries, but also the leap into electronic typesetting, remaining essentially unchanged. It was popularised in the 1960s with the release of Letraset sheets containing Lorem Ipsum passages, and more recently with desktop publishing software like Aldus PageMaker including versions of Lorem Ipsum.</div>
  <div class="abs" style="left:0;top:135px;width:272px;height:101px;background:#dedede"></div>
  <div class="abs" style="left:18px;top:138px;width:98px;height:96px;background:var(--dark)"></div>
  <div class="h-sans" style="left:24px;top:144px;color:var(--white)">Lorem Ipsum</div>
  <div class="txt light" style="left:24px;top:160px;width:86px;height:70px">Lorem Ipsum is simply dummy text of the printing and typesetting industry. Lorem Ipsum has been the industry's standard dummy text ever since the 1500s, when an unknown printer took a galley of type and scrambled it to make a type specimen book.</div>
  <div class="txt" style="left:125px;top:142px;width:133px;height:88px">Lorem Ipsum is simply dummy text of the printing and typesetting industry. Lorem Ipsum has been the industry's standard dummy text ever since the 1500s, when an unknown printer took a galley of type and scrambled it to make a type specimen book. It has survived not only five centuries, but also the leap into electronic typesetting, remaining essentially unchanged. It was popularised in the 1960s with the release of Letraset sheets containing Lorem Ipsum passages, and more recently with desktop publishing software like Aldus PageMaker including versions of Lorem Ipsum.</div>
  <div class="abs" style="left:0;top:236px;width:272px;height:74px;background:var(--mid)"></div>
  <div class="txt" style="left:21px;top:240px;width:236px;height:66px;color:#4f4f4f">Lorem Ipsum is simply dummy text of the printing and typesetting industry. Lorem Ipsum has been the industry's standard dummy text ever since the 1500s, when an unknown printer took a galley of type and scrambled it to make a type specimen book. It has survived not only five centuries, but also the leap into electronic typesetting, remaining essentially unchanged. It was popularised in the 1960s with the release of Letraset sheets containing Lorem Ipsum passages, and more recently with desktop publishing software like Aldus PageMaker including versions of Lorem Ipsum. Lorem Ipsum is simply dummy text of the printing and typesetting industry. Lorem Ipsum has been the industry's standard dummy text ever since the 1500s, when an unknown printer took a galley of type and scrambled it to make a type specimen book. It has survived not only five centuries, but also the leap into electronic typesetting, remaining essentially unchanged. It was popularised in the 1960s with the release of Letraset sheets containing Lorem Ipsum passages, and more recently with desktop publishing software like Aldus PageMaker including versions of Lorem Ipsum.</div>
  <div class="outline-box" style="left:24px;top:322px;width:232px;height:40px"></div>
  <div class="abs" style="left:104px;top:316px;width:66px;background:var(--page);font:400 9.5px/1 var(--sans);color:var(--ink);text-align:center">Lorem Ipsum</div>
  <div class="txt" style="left:33px;top:329px;width:214px;height:30px">Lorem Ipsum is simply dummy text of the printing and typesetting industry. Lorem Ipsum has been the industry's standard dummy text ever since the 1500s, when an unknown printer took a galley of type and scrambled it to make a type specimen book. It has survived not only five centuries, but also the leap into electronic typesetting, remaining essentially unchanged. It was popularised in the 1960s with the release of Letraset sheets containing Lorem Ipsum passages, and more recently with desktop publishing software like Aldus PageMaker including versions of Lorem Ipsum.</div>
  <div class="footbar"></div>
</section>

<!-- Page 6 : JV partners -->
<section class="page p6">
  <div class="strip"></div>
  <div class="url left">WWW.TARNWICKCOMMUNITIES.COM</div>
  <div class="pageno right">06</div>
  <div class="band" style="top:30px;height:52px"><div class="title" style="padding:8px 0 0 21px">We are offering our<br>JV partners</div></div>
  <div class="txt" style="left:21px;top:88px;width:114px;height:96px">Lorem Ipsum is simply dummy text of the printing and typesetting industry. Lorem Ipsum has been the industry's standard dummy text ever since the 1500s, when an unknown printer took a galley of type and scrambled it to make a type specimen book. It has survived not only five centuries, but also the leap into electronic typesetting, remaining essentially unchanged. It was popularised in the 1960s with the release of Letraset sheets containing Lorem Ipsum passages, and more recently with desktop publishing software like Aldus PageMaker including versions of Lorem Ipsum.</div>
  <div class="txt" style="left:144px;top:88px;width:114px;height:96px">Lorem Ipsum is simply dummy text of the printing and typesetting industry. Lorem Ipsum has been the industry's standard dummy text ever since the 1500s, when an unknown printer took a galley of type and scrambled it to make a type specimen book. It has survived not only five centuries, but also the leap into electronic typesetting, remaining essentially unchanged. It was popularised in the 1960s with the release of Letraset sheets containing Lorem Ipsum passages, and more recently with desktop publishing software like Aldus PageMaker including versions of Lorem Ipsum.</div>
  <div class="band" style="top:190px;height:52px"><div class="title" style="padding:8px 0 0 21px">Benefits and options<br>of model</div></div>
  <div class="txt" style="left:21px;top:249px;width:116px;height:122px">Lorem Ipsum is simply dummy text of the printing and typesetting industry. Lorem Ipsum has been the industry's standard dummy text ever since the 1500s, when an unknown printer took a galley of type and scrambled it to make a type specimen book. It has survived not only five centuries, but also the leap into electronic typesetting, remaining essentially unchanged. It was popularised in the 1960s with the release of Letraset sheets containing Lorem Ipsum passages, and more recently with desktop publishing software like Aldus PageMaker including versions of Lorem Ipsum. Lorem Ipsum is simply dummy text of the printing and typesetting industry. Lorem Ipsum has been the industry's standard dummy text ever since the 1500s, when an unknown printer took a galley of type and scrambled it to make a type specimen book.</div>
  <div class="photo" role="img" aria-label="Senior man in swim cap beside a pool" style="left:149px;top:247px;width:112px;height:124px;background:linear-gradient(160deg,#dbe8ef 0%,#5ea3c9 45%,#c9a18a 75%,#8aa6b5 100%)"></div>
  <div class="footbar"></div>
</section>

<!-- Page 7 : market difference -->
<section class="page p7">
  <div class="strip"></div>
  <div class="pageno left">07</div>
  <div class="url right">WWW.TARNWICKCOMMUNITIES.COM</div>
  <div class="band" style="top:30px;height:108px"><div class="title" style="padding:10px 0 0 21px;font-size:13.5px;line-height:1.4">How Tarwick will change the market for the better/ difference between us and old models</div></div>
  <div class="abs" style="left:19px;top:138px;width:123px;height:224px;background:var(--dark)"></div>
  <div class="txt light" style="left:27px;top:145px;width:108px;height:212px">Lorem Ipsum is simply dummy text of the printing and typesetting industry. Lorem Ipsum has been the industry's standard dummy text ever since the 1500s, when an unknown printer took a galley of type and scrambled it to make a type specimen book. It has survived not only five centuries, but also the leap into electronic typesetting, remaining essentially unchanged. It was popularised in the 1960s with the release of Letraset sheets containing Lorem Ipsum passages, and more recently with desktop publishing software like Aldus PageMaker including versions of Lorem Ipsum. Lorem Ipsum is simply dummy text of the printing and typesetting industry. Lorem Ipsum has been the industry's standard dummy text ever since the 1500s, when an unknown printer took a galley of type and scrambled it to make a type specimen book. It has survived not only five centuries, but also the leap into electronic typesetting, remaining essentially unchanged. It was popularised in the 1960s with the release of Letraset sheets containing Lorem Ipsum passages, and more recently with desktop publishing software like Aldus PageMaker including versions of Lorem Ipsum. Lorem Ipsum is simply dummy text of the printing and typesetting industry. Lorem Ipsum has been the industry's standard dummy text ever since the 1500s, when an unknown printer took a galley of type and scrambled it to make a type specimen book.</div>
  <div class="txt" style="left:151px;top:145px;width:108px;height:156px">Lorem Ipsum is simply dummy text of the printing and typesetting industry. Lorem Ipsum has been the industry's standard dummy text ever since the 1500s, when an unknown printer took a galley of type and scrambled it to make a type specimen book. It has survived not only five centuries, but also the leap into electronic typesetting, remaining essentially unchanged. It was popularised in the 1960s with the release of Letraset sheets containing Lorem Ipsum passages, and more recently with desktop publishing software like Aldus PageMaker including versions of Lorem Ipsum. Lorem Ipsum is simply dummy text of the printing and typesetting industry. Lorem Ipsum has been the industry's standard dummy text ever since the 1500s, when an unknown printer took a galley of type and scrambled it to make a type specimen book. It has survived not only five centuries, but also the leap into electronic typesetting, remaining essentially unchanged. It was popularised in the 1960s with the release of Letraset sheets containing Lorem Ipsum passages, and more recently with desktop publishing software like Aldus PageMaker including versions of Lorem Ipsum. Lorem Ipsum is simply dummy text of the printing and typesetting industry. Lorem Ipsum has been the industry's standard dummy text ever since the 1500s, when an unknown printer took a galley of type and scrambled it to make a type specimen book.</div>
  <div class="footbar"></div>
</section>

<!-- Page 8 : back cover -->
<section class="page p8">
  <div class="brand" style="top:25px"><div class="brand-name">TARNWICK</div><div class="brand-sub">COMMUNITIES</div></div>
  <div class="photo" role="img" aria-label="Group of seniors jumping joyfully on a sunny beach" style="left:0;top:70px;width:272px;height:182px;background:linear-gradient(180deg,#6f86a3 0%,#9fb1c2 40%,#b9b4ad 65%,#d9cdb9 100%)"></div>
  <div class="abs" style="left:0;top:258px;width:272px;height:61px;background:var(--dark)"></div>
  <div class="abs contact-title" style="left:19px;top:268px">Contact Us</div>
  <div class="abs contact-line" style="left:19px;top:290px">27 Harbour Lane, Westfield,<br>P.O.Box 48120, USA</div>
  <div class="abs contact-line" style="left:150px;top:290px">OFFICE: +1 555 0148 220<br>EMAIL: info@tarnwick.com</div>
  <div class="abs" style="left:19px;top:328px;font:400 15px/1 var(--serif);color:var(--ink)">Follow Us: <span class="social"></span><span class="social"></span></div>
  <div class="footbar"></div>
</section>

</div>
</body>
</html>
```